Book Cover " FROM GRAVEL TO AMBER"

Looking for a book cover for a novel from Gravel to Amber.
Amber is the characters developed name. The book describes his rough up bringing and how he obtains his greatness and his given name Amber.

```html
<!DOCTYPE html>
<html lang="en">
<head>
<meta charset="utf-8">
<title>From Gravel to Amber — Book Cover</title>
<link rel="stylesheet" href="https://fonts.googleapis.com/css2?family=Cinzel:wght@400&family=Great+Vibes&display=swap">
<style>
  :root {
    --smoke-light: #a88a80;
    --smoke-mid: #7d6470;
    --smoke-dark: #4e3f55;
    --gravel-light: #b8323a;
    --gravel-dark: #5a0c12;
    --silk-bright: #f04a5e;
    --silk-mid: #d4213a;
    --silk-deep: #8e0c20;
    --text-light: #fbf4f2;
    --title-red: #8c0f22;
    --glow: rgba(255, 240, 240, 0.85);
  }
  html, body {
    margin: 0;
    padding: 0;
    width: 811px;
    height: 1200px;
    overflow: hidden;
    background: #ffffff;
  }
  .cover {
    position: relative;
    width: 811px;
    height: 1200px;
    overflow: hidden;
  }
  .cover-art {
    position: absolute;
    inset: 0;
    width: 811px;
    height: 1200px;
  }
  .author-name {
    position: absolute;
    top: 78px;
    left: 0;
    width: 811px;
    margin: 0;
    text-align: center;
    font-family: "Cinzel", serif;
    font-weight: 400;
    font-size: 66px;
    line-height: 118px;
    letter-spacing: 3px;
    color: var(--text-light);
  }
  .title {
    position: absolute;
    left: 0;
    top: 0;
    width: 811px;
    height: 1200px;
    margin: 0;
    font-weight: 400;
  }
  .title-script {
    position: absolute;
    font-family: "Great Vibes", cursive;
    color: var(--text-light);
    text-shadow: 0 0 6px rgba(90, 0, 10, 0.6);
    line-height: 1;
  }
  .title-caps {
    position: absolute;
    font-family: "Cinzel", serif;
    color: var(--title-red);
    text-shadow: 0 0 3px var(--glow), 0 0 8px rgba(255, 220, 220, 0.6);
    line-height: 1;
    letter-spacing: 1px;
  }
  .title-from { left: 108px; top: 828px; font-size: 118px; }
  .title-gravel { left: 112px; top: 900px; font-size: 112px; }
  .title-to { left: 104px; top: 1010px; font-size: 118px; }
  .title-amber { left: 298px; top: 1002px; font-size: 112px; }
</style>
</head>
<body>
<main class="cover">
  <svg class="cover-art" viewBox="0 0 811 1200" xmlns="http://www.w3.org/2000/svg">
    <defs>
      <linearGradient id="smoke-fill" x1="0" y1="0" x2="1" y2="1">
        <stop offset="0" stop-color="var(--smoke-light)"/>
        <stop offset="0.45" stop-color="var(--smoke-mid)"/>
        <stop offset="1" stop-color="var(--smoke-dark)"/>
      </linearGradient>
      <radialGradient id="gravel-fill" cx="0.4" cy="0.3" r="0.8">
        <stop offset="0" stop-color="var(--gravel-light)"/>
        <stop offset="1" stop-color="var(--gravel-dark)"/>
      </radialGradient>
      <linearGradient id="silk-fill" x1="0" y1="0" x2="1" y2="1">
        <stop offset="0" stop-color="var(--silk-deep)"/>
        <stop offset="0.35" stop-color="var(--silk-mid)"/>
        <stop offset="0.6" stop-color="var(--silk-bright)"/>
        <stop offset="1" stop-color="var(--silk-mid)"/>
      </linearGradient>
    </defs>
    <rect role="img" aria-label="Soft mauve smoke drifting across the sky" x="0" y="0" width="811" height="620" fill="url(#smoke-fill)"/>
    <path role="img" aria-label="Red silk fabric draped in folds" d="M0 760 C200 800 500 770 811 740 L811 1200 L0 1200 Z" fill="url(#silk-fill)"/>
    <path role="img" aria-label="Field of coarse red glittering gravel" d="M0 540 C220 505 520 505 811 560 L811 700 C560 760 300 800 0 860 Z" fill="url(#gravel-fill)"/>
  </svg>

  <p class="author-name">AUTHOR<br>NAME</p>

  <h1 class="title">
    <span class="title-script title-from">From</span>
    <span class="title-caps title-gravel">GRAVEL</span>
    <span class="title-script title-to">To</span>
    <span class="title-caps title-amber">AMBER</span>
  </h1>
</main>
</body>
</html>
```